IT Company seeking creative modern BUSINESS CARD DESIGN!

We are a full service IT company located in California. We specialize in offering computer network support to small to medium to enterprise sized businesses. We are looking for a new business card design to go with our newly designed logo. We prefer business cards that are unique and make a lasting impression. We tend to like business cards with black, gray or blue backgrounds. Our color theme should include black, blue, gray and white only. We want something BOLD, BRIGHT, FUN, CLEAN, and MODERN. Please design with creativity in mind! :) We want our business cards to "pop" and "stand out" when compared to other business cards side by side. We want to be different and make that WINNING first impression every time!! =)

FONT NAME FOR harbor forge is "Cynthe" True Type font.

BLUE LOGO COLOR IS:
Hex: #2375BB
R: 35
G: 117
B: 187

The secondary color is pure "Black". Use of Grayscale is okay too.
Updates

Please look over the sample designs I attached. ** IMPORTANT ** This will give you an idea of the color, design and layouts we like. Also, our logo needs to stand out (nothing small and DO NOT duplicate logo twice on same side of the card. We do want a front and back to the card design. You are welcome to separate the circle logo and the business name if needed. Also, please no pastel colors or busy backgrounds with design. Watermark backgrounds would be okay if it works with the logo design. Let me know if you have any issues opening the logo or font file. Thanks a bunch! EXCITED and AWAITING your designs! I will provide as much feedback as possible. Thank you, Tova :)

Target Market(s)

Small, Medium to Enterprise businesses. Business Card will be given to professionals. We want the card to stand out and look and feel different.

Industry/Entity Type

Computer

Font styles to use
Sans Serif

Colors
0555a3
ffffff
000000
474747
959595
5c5c5c
c8c8c8
eeeeee
3276b5

Requirements
Must have
• WE WANT TO STAND OUT! BE DIFFERENT! MAKE A LASTING IMPRESSION!

We like clean, neat, modern, BOLD look. See attachment for samples of designs we like.

This is the information needed on the business card. Exact information will change per employee (of course), but heres the required data needed (this info can go on either the front or back of the business card).

Business Logo (File attached)

Gary Loftis
CEO / Senior Network Engineer
7381 Delacroix Avenue
Suite D
Modesto, CA 95871

main tel: 209-555-0172
direct tel: 209-555-0139
cell: 209-555-0186
fax tel: 209-xxx-xxxx

gloftis@hfqx.example
www.hfqx.example

We really like the use of icons for the address, phone, location etc. Looks modern and clean.

Nice to have
• Somewhere it would be nice to include the cities we are located in and serving:
Modesto - Fresno - Stockton - Pleasanton (FYI - if there's no design space to include these cities, then that's okay. This is just a wish list item to include if theres room. =)

We like watermark background effects if that's an option. Not necessary though.

If there's a way to include we are on Face Book, Linked In, and Twitter - that would be cool, but not necessary.

Different Card Size or cut ot rounded edges might be cool, but not necessary. We do want to STAND OUT and be different.
Should not have
• No other colors other than Blue, Black, Gray, White. Do not like pastel blue or light blue. For lighter coloring.... would prefer gray scale or white. Keep BLUE color bold and vibrant (like samples I attached).

Do not do a traditional white business card. Too boring and ordinary. Do not make address and phone information in large fat fonts. We want neat and tidy - modern looking fonts. :)

```html
<!DOCTYPE html>
<html lang="en">
<head>
<meta charset="utf-8">
<title>harbor forge — business cards</title>
<link rel="stylesheet" href="https://fonts.googleapis.com/css2?family=Arimo:wght@400;700&family=Roboto+Condensed:wght@400;700&display=swap">
<style>
  :root {
    --backdrop: #33403f;
    --card: #222222;
    --card-edge: #111111;
    --blue: #2375bb;
    --white: #ffffff;
    --ink-dark: #1b1b1b;
  }
  html, body {
    margin: 0;
    width: 900px;
    height: 1200px;
    overflow: hidden;
    background: var(--backdrop);
  }
  .stage { display: block; width: 900px; height: 1200px; }
  .card-face { fill: var(--card); stroke: var(--card-edge); stroke-width: 1.5; }
  .brand-band, .ribbon { fill: var(--blue); }
  .emblem-cradle { fill: var(--card); }
  .emblem-ring { fill: var(--white); }
  .emblem-core { fill: var(--blue); }
  .wordmark {
    font-family: "Arimo", Arial, sans-serif;
    font-weight: 700;
    fill: var(--blue);
  }
  .person-name {
    font-family: "Roboto Condensed", "Arial Narrow", sans-serif;
    font-weight: 700;
    font-size: 29px;
    fill: var(--white);
  }
  .person-role {
    font-family: "Roboto Condensed", "Arial Narrow", sans-serif;
    font-size: 14px;
    fill: var(--white);
  }
  .contact {
    font-family: "Arimo", Arial, sans-serif;
    font-size: 16px;
    fill: var(--white);
  }
  .timeline { stroke: var(--blue); stroke-width: 2.5; fill: none; }
  .icon-dot { fill: var(--blue); }
  .icon-glyph { fill: var(--white); }
  .icon-stroke { fill: none; stroke: var(--white); stroke-width: 1.6; }
</style>
</head>
<body>
<svg class="stage" viewBox="0 0 900 1200" xmlns="http://www.w3.org/2000/svg">

  <!-- Front of card -->
  <g class="card-front">
    <rect class="card-face" x="76" y="122" width="750" height="438"/>
    <rect class="brand-band" x="77" y="260" width="748" height="92"/>
    <circle class="emblem-cradle" cx="450" cy="306" r="96"/>
    <circle class="emblem-ring" cx="450" cy="306" r="66"/>
    <circle class="emblem-core" cx="450" cy="306" r="60"/>
    <text class="wordmark" x="450" y="422" font-size="40" text-anchor="middle">harbor forge</text>
  </g>

  <!-- Back of card -->
  <g class="card-back">
    <rect class="card-face" x="76" y="641" width="750" height="439"/>

    <path class="ribbon" d="M143 642 H245 V782 Q194 758 143 782 Z"/>
    <path class="ribbon" d="M143 1079 H245 V1020 Q194 1044 143 1020 Z"/>

    <circle class="emblem-ring" cx="194" cy="703" r="38"/>
    <circle class="emblem-core" cx="194" cy="703" r="34"/>

    <text class="person-name" transform="translate(186 1010) rotate(-90)">GARY LOFTIS</text>
    <text class="person-role" transform="translate(219 1010) rotate(-90)">CEO / Jaringan Senior Insinyur</text>

    <text class="wordmark" x="275" y="717" font-size="40">harbor forge</text>

    <text class="contact" x="527" y="862" text-anchor="middle">7381 Delacroix Street, Suite D</text>
    <text class="contact" x="527" y="882" text-anchor="middle">Modesto, CA 95871</text>

    <line class="timeline" x1="305" y1="927" x2="768" y2="927"/>
    <line class="timeline" x1="370" y1="946" x2="370" y2="956"/>
    <line class="timeline" x1="536" y1="898" x2="536" y2="908"/>
    <line class="timeline" x1="536" y1="946" x2="536" y2="956"/>
    <line class="timeline" x1="706" y1="946" x2="706" y2="956"/>

    <!-- phone icon -->
    <circle class="icon-dot" cx="370" cy="927" r="19"/>
    <path class="icon-glyph" d="M359 922 Q370 914 381 922 L379 926 L375 925 L374 922 Q370 921 366 922 L365 925 L361 926 Z"/>
    <rect class="icon-glyph" x="362" y="926" width="16" height="10" rx="2"/>

    <!-- home icon -->
    <circle class="icon-dot" cx="536" cy="927" r="19"/>
    <path class="icon-glyph" d="M524 928 L536 917 L548 928 H545 V938 H539 V931 H533 V938 H527 V928 Z"/>

    <!-- globe icon -->
    <circle class="icon-dot" cx="706" cy="927" r="19"/>
    <circle class="icon-stroke" cx="706" cy="927" r="10"/>
    <ellipse class="icon-stroke" cx="706" cy="927" rx="4.5" ry="10"/>
    <line class="icon-stroke" x1="696" y1="927" x2="716" y2="927"/>
    <line class="icon-stroke" x1="698" y1="921" x2="714" y2="921"/>
    <line class="icon-stroke" x1="698" y1="933" x2="714" y2="933"/>

    <text class="contact" x="317" y="981">209 555 0172</text>
    <text class="contact" x="317" y="1001">209 555 0139</text>
    <text class="contact" x="317" y="1021">209 555 0186</text>

    <text class="contact" x="707" y="981" text-anchor="middle">gloftis@hfqx.example</text>
    <text class="contact" x="707" y="1001" text-anchor="middle">www.hfqx.example</text>
  </g>
</svg>
</body>
</html>
```